Plakat-Design Workshop gegen Prüfungsangst
Zielgruppe
Prüfungsangst überwinden mittels Workshops: 'Selbsthypnose erlernen'
Zielgruppe Studenten
Schweißausbrüche, Blackout, und Resignation.
Viele kennen diese unangenehmen Momente, wenn eine Prüfung begonnen hat und die Aufgabenstellungen scheinbar unlösbar sind.
Dann ist Entspannung nahezu unmöglich. Das Stresshormon Cortisol wurde bereits ausgeschüttet. Es beeinträchtigt die Erinnerung an das Gelernte.
Die mentale Vorbereitung sollte schon viel eher ansetzen, wenn es noch nicht zu spät ist. Wenn der Körper noch nicht verkrampft ist.
Selbsthypnose vor Prüfungen ist hier eine tolle Möglichkeit.
Mit Hilfe einer geführten Selbsthypnoseanleitung ist es Dir möglich Dein Unterbewusstsein so zu programmieren, dass diese Übererregungszustände vor Prüfungssituationen deutlich reduziert werden.
Aufgabenstellung
DINA 4 Plakat, 'Prüfungsangst?' mit einem Freifeld, wo man Ort, Datum und Zeit der Veranstaltung 'Selbsthypnose erlernen'
(Selbstsicher in die Prüfung) eindrucken kann.
darunter:
Anmeldung: Tel: 01563 8274015
Dipl. Sportl. Henrik Malow Mentaltraining
weitere Infos auch über Einzelsitzungen: www.malow-trance.de

```html
<!DOCTYPE html>
<html lang="de">
<head>
<meta charset="utf-8">
<title>Prüfungsangst – Workshop Selbsthypnose</title>
<link rel="stylesheet" href="https://fonts.googleapis.com/css2?family=Fira+Sans:wght@400;500;600&display=swap">
<style>
  :root {
    --red: #e2302a;
    --ink: #111111;
    --paper: #ffffff;
    --rule: #a9a9a9;
    --photo-warm-1: #b8773a;
    --photo-warm-2: #8a6a55;
    --photo-cool: #9fb0c8;
    --portrait-1: #b9b9b6;
    --portrait-2: #6f7680;
    --badge-ring: #c9d3d8;
    --badge-core: #1d8494;
  }
  html, body {
    margin: 0;
    padding: 0;
    width: 881px;
    height: 1200px;
    overflow: hidden;
    background: var(--paper);
  }
  .poster {
    position: relative;
    width: 881px;
    height: 1200px;
    background: var(--paper);
    font-family: "Fira Sans", sans-serif;
    color: var(--ink);
    overflow: hidden;
  }
  .hero-photo {
    position: absolute;
    left: 0; top: 0;
    width: 881px; height: 382px;
    background: linear-gradient(100deg, var(--photo-warm-1) 0%, var(--photo-warm-2) 45%, var(--photo-cool) 80%, #d7d9de 100%);
  }
  .hero-rule {
    position: absolute;
    left: 0; top: 388px;
    width: 881px; height: 5px;
    background: var(--red);
  }
  .headline {
    position: absolute;
    left: 30px; top: 400px;
    margin: 0;
    font-size: 113px;
    font-weight: 500;
    letter-spacing: -1.5px;
    line-height: 1;
    color: var(--red);
  }
  .symptoms {
    position: absolute;
    left: 32px; top: 532px;
    margin: 0;
    font-size: 37px;
    font-weight: 600;
    letter-spacing: -0.3px;
  }
  .intro {
    position: absolute;
    left: 32px; top: 586px;
    margin: 0;
    font-size: 26.5px;
    font-weight: 400;
    line-height: 38px;
  }
  .claim {
    position: absolute;
    left: 31px; top: 716px;
    margin: 0;
    font-size: 66px;
    font-weight: 500;
    letter-spacing: -0.8px;
    line-height: 1;
    color: var(--red);
  }
  .portrait {
    position: absolute;
    left: 33px; top: 810px;
    width: 247px; height: 338px;
    background: linear-gradient(160deg, var(--portrait-1) 0%, #9ea2a8 55%, var(--portrait-2) 100%);
  }
  .badge {
    position: absolute;
    left: 225px; top: 1030px;
    width: 160px; height: 160px;
    z-index: 2;
  }
  .event-fields {
    position: absolute;
    left: 405px; top: 800px;
    width: 445px;
  }
  .field {
    display: flex;
    align-items: flex-end;
    height: 67px;
    font-size: 42px;
    font-weight: 400;
  }
  .field-label { line-height: 1; padding-bottom: 2px; }
  .field-blank {
    flex: 1;
    margin-left: 4px;
    margin-bottom: 6px;
    border-bottom: 2px solid var(--rule);
  }
  .registration {
    position: absolute;
    left: 406px; top: 1006px;
    font-size: 21.5px;
    line-height: 28.5px;
  }
  .registration p { margin: 0; }
  .registration strong { font-weight: 600; }
  .footer-band {
    position: absolute;
    left: 0; top: 1160px;
    width: 881px; height: 40px;
    background: var(--red);
  }
</style>
</head>
<body>
<main class="poster">
  <div class="hero-photo" role="img" aria-label="Foto: gestresste Studentin hält sich in einer Prüfungshalle den Kopf, dahinter weitere Prüflinge an Tischen"></div>
  <div class="hero-rule"></div>

  <h1 class="headline">Prüfungsangst?</h1>
  <h2 class="symptoms">Schweißausbrüche, Blackout &amp; Resignation?</h2>
  <p class="intro">Im Workshop "Selbsthypnose" lernst Du Strategien, solche<br>Übererregungszustände vor Prüfungen deutlich zu reduzieren.</p>

  <h2 class="claim">Selbstsicher in die Prüfung!</h2>

  <div class="portrait" role="img" aria-label="Porträtfoto des Mentaltrainers im hellblauen Hemd vor einer Betonwand"></div>

  <svg class="badge" viewBox="0 0 160 160" aria-label="Zertifikatssiegel">
    <circle cx="80" cy="80" r="78" fill="#ffffff"/>
    <circle cx="80" cy="80" r="68" fill="var(--badge-ring)" stroke="var(--badge-core)" stroke-width="2"/>
    <circle cx="80" cy="80" r="36" fill="var(--badge-core)"/>
  </svg>

  <section class="event-fields">
    <div class="field"><span class="field-label">Ort:</span><span class="field-blank"></span></div>
    <div class="field"><span class="field-label">Datum:</span><span class="field-blank"></span></div>
    <div class="field"><span class="field-label">Zeit:</span><span class="field-blank"></span></div>
  </section>

  <section class="registration">
    <p><strong>Anmeldung:</strong></p>
    <p>Tel: 01563 8274015</p>
    <p>Dipl. Sportl. Henrik Malow Mentaltraining</p>
    <p>weitere Infos auch über Einzelsitzungen:</p>
    <p><strong>www.malow-trance.de</strong></p>
  </section>

  <div class="footer-band"></div>
</main>
</body>
</html>
```